Sports Field sign

Our business provides audio visual solutions to corporate and government clients. We have purchased space at a sports field to place two signs to promote our business. We need to provide the artwork in high res format for a sign to be placed at a sports oval. The physical sign will be 900mm high and 7000mm long. It needs to include our logo, contact number, and the services we offer. It needs to be tidy, easy to read and easily visible from a distance. The sample I have done is very basic but covers what we need - I would expect that a designer can produce an eye-catching impressive sign with this much space to work with., and may even include some flashy background, an image or creative design to get attention.

examples of what signs are up at the oval now here - https://chirpline.example/GRL/status/4820913375561029417?s=31&t=8-qLmR3kdopyTUwZcQ_xP

Our Company web site is www.brightmesh.example.au

```html
<!DOCTYPE html>
<html lang="en">
<head>
<meta charset="utf-8">
<title>brightmesh systems – sports field sign options</title>
<link rel="stylesheet" href="https://fonts.googleapis.com/css2?family=Barlow+Condensed:ital,wght@0,600;0,700;1,800&family=Montserrat:wght@400;700;800&family=Open+Sans:wght@400&display=swap">
<style>
  :root {
    --blue: #2c58a6;
    --orange: #f26522;
    --black: #000000;
    --white: #ffffff;
    --board: #bdbdbd;
    --label: #1e1e1e;
    --divider: #8a8a8a;
  }
  * { margin: 0; padding: 0; box-sizing: border-box; }
  html, body { width: 1200px; height: 886px; overflow: hidden; }
  body { background: var(--board); position: relative; font-family: "Montserrat", sans-serif; }

  .option-label {
    position: absolute; left: 49px;
    font: 400 18px/1 "Montserrat", sans-serif;
    color: var(--label); letter-spacing: 0.5px;
  }
  .sign {
    position: absolute; left: 49px; width: 1101px; height: 141px; display: block;
    filter: drop-shadow(0 2px 3px rgba(0,0,0,0.35));
  }
  .sign text { white-space: pre; }

  .brand-name { font-family: "Open Sans", sans-serif; font-weight: 400; }
  .tagline { font-family: "Open Sans", sans-serif; font-weight: 400; }
  .pillars { font-family: "Montserrat", sans-serif; font-weight: 700; }
  .service-list { font-family: "Barlow Condensed", sans-serif; font-weight: 600; }
  .service-caps { font-family: "Barlow Condensed", sans-serif; font-weight: 800; font-style: italic; }
  .phone-condensed { font-family: "Barlow Condensed", sans-serif; font-weight: 700; }
  .phone-wide { font-family: "Montserrat", sans-serif; font-weight: 800; }
  .cities { font-family: "Montserrat", sans-serif; font-weight: 700; }

  .fill-white { fill: var(--white); }
  .fill-black { fill: var(--black); }
  .fill-blue { fill: var(--blue); }
  .fill-orange { fill: var(--orange); }
  .stroke-orange { stroke: var(--orange); }
  .stroke-divider { stroke: var(--divider); }
</style>
</head>
<body>

<svg width="0" height="0" style="position:absolute" aria-hidden="true">
  <defs>
    <symbol id="handset" viewBox="0 0 85 85">
      <path d="M27 14c4-2 8 0 9 4l4 12c1 4-1 7-4 8l-4 1c2 11 7 20 14 26l4-1c3-1 6 0 8 3l6 9c2 3 1 7-2 9l-5 3c-7 3-15-1-22-10c-11-14-16-33-14-55c1-5 3-8 6-9z"/>
    </symbol>
  </defs>
</svg>

<!-- Option 1 -->
<div class="option-label" style="top:21px">SAMPLE 1</div>
<svg class="sign" style="top:49px" viewBox="0 0 2054 263" preserveAspectRatio="none">
  <rect width="2054" height="263" class="fill-white"/>
  <polygon points="0,199 938,199 914,263 0,263" class="fill-blue"/>
  <polygon points="996,0 1010,0 932,199 918,199" class="fill-blue"/>
  <polygon points="1022,0 1512,0 1446,183 2054,183 2054,263 918,263" class="fill-black"/>
  <rect x="1442" y="183" width="612" height="16" class="fill-blue"/>
  <polygon points="1512,0 1526,0 1458,183 1444,183" class="fill-blue"/>

  <rect x="120" y="42" width="130" height="130" class="fill-blue"/>
  <text x="369" y="107" font-size="64" class="brand-name fill-black" textLength="490" lengthAdjust="spacingAndGlyphs">brightmesh systems</text>
  <line x1="369" y1="124" x2="860" y2="124" stroke-width="4" class="stroke-orange"/>
  <text x="369" y="158" font-size="24" class="tagline fill-black" textLength="450" lengthAdjust="spacingAndGlyphs">BRINGING PEOPLE TOGETHER WITH TECH</text>
  <text x="32" y="247" font-size="36" class="pillars fill-white" textLength="864" lengthAdjust="spacingAndGlyphs">DESIGN - CONSULTING - SERVICE - MAINTENANCE</text>

  <polygon points="1048,28 1068,40 1044,52" class="fill-orange"/>
  <polygon points="1033,71 1053,83 1029,95" class="fill-orange"/>
  <polygon points="1016,113 1036,125 1012,137" class="fill-orange"/>
  <polygon points="1002,156 1022,168 998,180" class="fill-orange"/>
  <text x="1095" y="52" font-size="40" class="service-caps fill-white" textLength="368" lengthAdjust="spacingAndGlyphs">VIDEO CONFERENCING</text>
  <text x="1078" y="95" font-size="40" class="service-caps fill-white" textLength="276" lengthAdjust="spacingAndGlyphs">DIGITAL SIGNAGE</text>
  <text x="1061" y="137" font-size="40" class="service-caps fill-white" textLength="306" lengthAdjust="spacingAndGlyphs">L.E.D VIDEO WALLS</text>
  <text x="1046" y="180" font-size="40" class="service-caps fill-white" textLength="302" lengthAdjust="spacingAndGlyphs">AUDIO SOLUTIONS</text>

  <rect x="1520" y="74" width="54" height="56" rx="8" class="fill-blue"/>
  <use href="#handset" x="1524" y="78" width="46" height="48" class="fill-white"/>
  <text x="1598" y="136" font-size="104" class="phone-condensed fill-black" textLength="428" lengthAdjust="spacingAndGlyphs">1300 555 417</text>

  <text x="1004" y="248" font-size="44" class="cities fill-white" textLength="274" lengthAdjust="spacingAndGlyphs">MELBOURNE</text>
  <circle cx="1313" cy="233" r="9" class="fill-orange"/>
  <text x="1348" y="248" font-size="44" class="cities fill-white" textLength="178" lengthAdjust="spacingAndGlyphs">SYDNEY</text>
  <circle cx="1559" cy="233" r="9" class="fill-orange"/>
  <text x="1597" y="248" font-size="44" class="cities fill-white" textLength="218" lengthAdjust="spacingAndGlyphs">BRISBANE</text>
  <circle cx="1851" cy="233" r="9" class="fill-orange"/>
  <text x="1886" y="248" font-size="44" class="cities fill-white" textLength="140" lengthAdjust="spacingAndGlyphs">PERTH</text>
</svg>

<!-- Option 2 -->
<div class="option-label" style="top:230px">SAMPLE 2</div>
<svg class="sign" style="top:257px" viewBox="0 0 2054 263" preserveAspectRatio="none">
  <rect width="2054" height="263" class="fill-white"/>
  <rect x="0" y="205" width="990" height="58" class="fill-black"/>
  <polygon points="892,0 2054,0 2054,71 918,71" class="fill-orange"/>
  <polygon points="918,71 2054,71 2054,263 984,263" class="fill-blue"/>

  <rect x="120" y="35" width="135" height="135" class="fill-blue"/>
  <text x="380" y="98" font-size="68" class="brand-name fill-black" textLength="498" lengthAdjust="spacingAndGlyphs">brightmesh systems</text>
  <line x1="380" y1="121" x2="880" y2="121" stroke-width="4" class="stroke-orange"/>
  <text x="380" y="154" font-size="25" class="tagline fill-black" textLength="458" lengthAdjust="spacingAndGlyphs">BRINGING PEOPLE TOGETHER WITH TECH</text>
  <text x="37" y="249" font-size="38" class="pillars fill-white" textLength="898" lengthAdjust="spacingAndGlyphs">DESIGN - CONSULTING - SERVICE - MAINTENANCE</text>

  <text x="941" y="51" font-size="36" class="service-list fill-white" textLength="1075" lengthAdjust="spacingAndGlyphs">Video Conferencing  |  Digital Signage  |  L.E.D Video Walls  |  Audio Solutions</text>

  <rect x="1022" y="91" width="85" height="87" rx="12" class="fill-white"/>
  <use href="#handset" x="1026" y="95" width="77" height="79" class="fill-blue"/>
  <text x="1141" y="176" font-size="128" class="phone-wide fill-white" textLength="868" lengthAdjust="spacingAndGlyphs">1300 555 417</text>

  <text x="1026" y="243" font-size="44" class="cities fill-white" textLength="268" lengthAdjust="spacingAndGlyphs">MELBOURNE</text>
  <circle cx="1329" cy="227" r="8" class="fill-orange"/>
  <text x="1364" y="243" font-size="44" class="cities fill-white" textLength="172" lengthAdjust="spacingAndGlyphs">SYDNEY</text>
  <circle cx="1569" cy="227" r="8" class="fill-orange"/>
  <text x="1606" y="243" font-size="44" class="cities fill-white" textLength="214" lengthAdjust="spacingAndGlyphs">BRISBANE</text>
  <circle cx="1855" cy="227" r="8" class="fill-orange"/>
  <text x="1889" y="243" font-size="44" class="cities fill-white" textLength="138" lengthAdjust="spacingAndGlyphs">PERTH</text>
</svg>

<!-- Option 3 -->
<div class="option-label" style="top:439px">SAMPLE 3</div>
<svg class="sign" style="top:467px" viewBox="0 0 2054 263" preserveAspectRatio="none">
  <rect width="2054" height="263" class="fill-white"/>
  <line x1="946" y1="25" x2="946" y2="175" stroke-width="2" class="stroke-divider"/>
  <rect x="0" y="191" width="1000" height="72" class="fill-black"/>
  <polygon points="954,191 2054,191 2054,263 984,263" class="fill-blue"/>

  <rect x="120" y="35" width="135" height="135" class="fill-blue"/>
  <text x="380" y="98" font-size="68" class="brand-name fill-black" textLength="498" lengthAdjust="spacingAndGlyphs">brightmesh systems</text>
  <line x1="380" y1="121" x2="880" y2="121" stroke-width="4" class="stroke-orange"/>
  <text x="380" y="154" font-size="25" class="tagline fill-black" textLength="458" lengthAdjust="spacingAndGlyphs">BRINGING PEOPLE TOGETHER WITH TECH</text>
  <text x="37" y="243" font-size="38" class="pillars fill-orange" textLength="898" lengthAdjust="spacingAndGlyphs">DESIGN - CONSULTING - SERVICE - MAINTENANCE</text>

  <text x="1019" y="43" font-size="36" class="service-list fill-black" textLength="997" lengthAdjust="spacingAndGlyphs">Video Conferencing  |  Digital Signage  |  L.E.D Video Walls  |  Audio Solutions</text>
  <line x1="1019" y1="61" x2="2016" y2="61" stroke-width="2" class="stroke-orange"/>

  <rect x="1022" y="82" width="85" height="86" rx="12" class="fill-orange"/>
  <use href="#handset" x="1026" y="86" width="77" height="78" class="fill-white"/>
  <text x="1129" y="165" font-size="128" class="phone-wide fill-black" textLength="892" lengthAdjust="spacingAndGlyphs">1300 555 417</text>

  <text x="1026" y="241" font-size="44" class="cities fill-white" textLength="268" lengthAdjust="spacingAndGlyphs">MELBOURNE</text>
  <circle cx="1329" cy="228" r="8" class="fill-orange"/>
  <text x="1364" y="241" font-size="44" class="cities fill-white" textLength="172" lengthAdjust="spacingAndGlyphs">SYDNEY</text>
  <circle cx="1569" cy="228" r="8" class="fill-orange"/>
  <text x="1606" y="241" font-size="44" class="cities fill-white" textLength="214" lengthAdjust="spacingAndGlyphs">BRISBANE</text>
  <circle cx="1855" cy="228" r="8" class="fill-orange"/>
  <text x="1889" y="241" font-size="44" class="cities fill-white" textLength="138" lengthAdjust="spacingAndGlyphs">PERTH</text>
</svg>

<!-- Option 4 -->
<div class="option-label" style="top:657px">SAMPLE 4</div>
<svg class="sign" style="top:685px" viewBox="0 0 2054 263" preserveAspectRatio="none">
  <rect width="2054" height="263" class="fill-white"/>
  <rect x="0" y="0" width="962" height="197" class="fill-black"/>
  <rect x="0" y="197" width="962" height="66" class="fill-orange"/>
  <rect x="962" y="197" width="1092" height="66" class="fill-blue"/>

  <rect x="122" y="38" width="135" height="135" class="fill-blue"/>
  <text x="384" y="102" font-size="68" class="brand-name fill-white" textLength="498" lengthAdjust="spacingAndGlyphs">brightmesh systems</text>
  <line x1="384" y1="125" x2="884" y2="125" stroke-width="4" class="stroke-orange"/>
  <text x="384" y="160" font-size="25" class="tagline fill-white" textLength="458" lengthAdjust="spacingAndGlyphs">BRINGING PEOPLE TOGETHER WITH TECH</text>
  <text x="37" y="249" font-size="38" class="pillars fill-white" textLength="898" lengthAdjust="spacingAndGlyphs">DESIGN - CONSULTING - SERVICE - MAINTENANCE</text>

  <text x="994" y="44" font-size="36" class="service-list fill-black" textLength="1022" lengthAdjust="spacingAndGlyphs">Video Conferencing  |  Digital Signage  |  L.E.D Video Walls  |  Audio Solutions</text>
  <line x1="994" y1="63" x2="2016" y2="63" stroke-width="2" class="stroke-orange"/>

  <rect x="997" y="87" width="87" height="88" rx="12" class="fill-orange"/>
  <use href="#handset" x="1001" y="91" width="79" height="80" class="fill-white"/>
  <text x="1107" y="177" font-size="134" class="phone-wide fill-black" textLength="906" lengthAdjust="spacingAndGlyphs">1300 555 417</text>

  <text x="1001" y="244" font-size="44" class="cities fill-white" textLength="268" lengthAdjust="spacingAndGlyphs">MELBOURNE</text>
  <circle cx="1302" cy="230" r="8" class="fill-orange"/>
  <text x="1338" y="244" font-size="44" class="cities fill-white" textLength="172" lengthAdjust="spacingAndGlyphs">SYDNEY</text>
  <circle cx="1542" cy="230" r="8" class="fill-orange"/>
  <text x="1580" y="244" font-size="44" class="cities fill-white" textLength="214" lengthAdjust="spacingAndGlyphs">BRISBANE</text>
  <circle cx="1829" cy="230" r="8" class="fill-orange"/>
  <text x="1864" y="244" font-size="44" class="cities fill-white" textLength="138" lengthAdjust="spacingAndGlyphs">PERTH</text>
</svg>

</body>
</html>
```